Label for LiPo Battery Product for RC Hobby Industry

We need your creativity for a new lithium battery label design. We aim to make our product visually appealing and distinct from competitors. Your design skills are crucial for this task, and we're excited to work with you.
Our main label feature is the colour tag profile, designed to easily identify battery category and power level with a 2-way colour band. Inspired by a tool company that uses a consistent colour profile to identify Phillips head sizing across their range.
The design should be modern, clear, convey speed and suitable for both professional and consumer markets.
Target Market(s)
RC, Drone, Camera community. 20-30 year old.
Industry/Entity Type
Battery, Drone Industry, RC Car
Requirements
Must have
- 2-Way colour tag identity profiling, clear text at 100% scale
Nice to have
- Text and graphic alignment. Comfortable padding and formatting. Colour tag profile, clear text."
Should not have
- Basic, stock looking image.

```html
<!DOCTYPE html>
<html lang="en">
<head>
<meta charset="utf-8">
<title>KELVRA T7 180 – LiPo Battery Label</title>
<link rel="stylesheet" href="https://fonts.googleapis.com/css2?family=Russo+One&family=Exo+2:wght@400;500&display=swap">
<style>
  :root {
    --page: #ffffff;
    --frame: #ffffff;
    --body-light: #3b3c40;
    --body-dark: #121214;
    --tag-red: #be1e2d;
    --tag-blue: #00aeef;
    --ink: #ffffff;
    --panel-tint: rgba(255, 255, 255, 0.05);
  }
  html, body {
    margin: 0;
    padding: 0;
    width: 1200px;
    height: 927px;
    overflow: hidden;
    background: var(--page);
  }
  .battery-label {
    display: block;
    width: 1200px;
    height: 927px;
  }
  .display-type {
    font-family: "Russo One", sans-serif;
    fill: var(--ink);
  }
  .feature-type {
    font-family: "Exo 2", sans-serif;
    font-weight: 500;
    font-size: 24px;
    fill: var(--ink);
  }
  .tag-red { fill: var(--tag-red); }
  .tag-blue { fill: var(--tag-blue); }
  .icon-line {
    fill: none;
    stroke: var(--ink);
    stroke-width: 2.4;
    stroke-linecap: round;
    stroke-linejoin: round;
  }
  .chevron {
    fill: none;
    stroke: var(--ink);
    stroke-width: 5;
    stroke-linecap: round;
    stroke-linejoin: round;
  }
</style>
</head>
<body>
<svg class="battery-label" viewBox="0 0 1200 927" xmlns="http://www.w3.org/2000/svg" role="img" aria-label="KELVRA T7 180 LiPo battery label: 1.3Ah, 120C, 6 cells, 22.2V, 1300Wh">
  <defs>
    <linearGradient id="labelBody" x1="0" y1="1" x2="1" y2="0">
      <stop offset="0" stop-color="var(--body-light)"/>
      <stop offset="0.55" stop-color="#2a2b2e"/>
      <stop offset="1" stop-color="var(--body-dark)"/>
    </linearGradient>
    <filter id="frameShadow" x="-5%" y="-5%" width="110%" height="115%">
      <feDropShadow dx="0" dy="3" stdDeviation="4" flood-color="#000" flood-opacity="0.25"/>
    </filter>
    <clipPath id="bodyClip">
      <rect x="103" y="187" width="995" height="553" rx="22"/>
    </clipPath>
  </defs>

  <rect class="label-frame" x="91" y="176" width="1018" height="576" rx="30" fill="var(--frame)" filter="url(#frameShadow)"/>

  <g clip-path="url(#bodyClip)">
    <rect class="label-body" x="103" y="187" width="995" height="553" fill="url(#labelBody)"/>
    <rect class="colour-tag tag-red" x="103" y="187" width="43" height="553"/>
    <rect class="colour-tag tag-blue" x="145" y="187" width="45" height="553"/>
    <polygon class="spec-panel" points="846,222 1098,222 1098,440 736,440" fill="var(--panel-tint)"/>
    <polygon class="feature-strip" points="283,608 1098,608 1098,697 220,697" fill="var(--panel-tint)"/>
  </g>

  <text class="display-type brand-name" x="239" y="309" font-size="80" textLength="327" lengthAdjust="spacingAndGlyphs">KELVRA</text>

  <text class="display-type model-code" x="197" y="507" font-size="200" textLength="458" lengthAdjust="spacingAndGlyphs">T7</text>
  <text class="display-type model-rating" x="668" y="578" font-size="145" textLength="417" lengthAdjust="spacingAndGlyphs">180</text>
  <text class="display-type capacity" x="291" y="582" font-size="70" textLength="232" lengthAdjust="spacingAndGlyphs">1.3AH</text>

  <g class="spec-list">
    <polyline class="chevron" points="808,240 822,251 808,262"/>
    <text class="display-type" x="867" y="268" font-size="48" textLength="114" lengthAdjust="spacingAndGlyphs">120C</text>
    <polyline class="chevron" points="793,294 807,305 793,316"/>
    <text class="display-type" x="845" y="321" font-size="46" textLength="179" lengthAdjust="spacingAndGlyphs">6 CELLS</text>
    <polyline class="chevron" points="779,347 793,358 779,369"/>
    <text class="display-type" x="830" y="374" font-size="46" textLength="123" lengthAdjust="spacingAndGlyphs">22.2V</text>
    <polyline class="chevron" points="766,401 780,412 766,423"/>
    <text class="display-type" x="817" y="428" font-size="46" textLength="192" lengthAdjust="spacingAndGlyphs">1300WH</text>
  </g>

  <g class="feature armour">
    <path class="icon-line" d="M308,639 L325,645 C325,660 320,670 308,676 C296,670 291,660 291,645 Z"/>
    <path class="icon-line" d="M308,645 L319,649 C319,659 315,665 308,669 C301,665 297,659 297,649 Z"/>
    <text class="feature-type" x="340" y="652">ARMOUR</text>
    <text class="feature-type" x="340" y="676">PROTECTION</text>
  </g>
  <g class="feature performance">
    <path class="icon-line" d="M551,667 A20,20 0 1 1 591,667 L584,667"/>
    <line class="icon-line" x1="566" y1="665" x2="580" y2="655" stroke-width="4"/>
    <text class="feature-type" x="613" y="664">PERFORMANCE</text>
  </g>
  <g class="feature insulation">
    <g class="icon-line">
      <line x1="882" y1="634" x2="882" y2="670"/>
      <line x1="866" y1="643" x2="898" y2="661"/>
      <line x1="866" y1="661" x2="898" y2="643"/>
      <polyline points="877,637 882,642 887,637"/>
      <polyline points="877,667 882,662 887,667"/>
    </g>
    <text class="feature-type" x="918" y="650">ADVANCED</text>
    <text class="feature-type" x="918" y="674">INSULATION</text>
  </g>
</svg>
</body>
</html>
```